Lorvika.no is a new website about pedagogical entrepreneurship. It's main target group is teachers. The Fjellmark Institute for Classroom Media and the Nordvik Agency for Schools and Study are leading the project.

The web page is meant to show examples of how different methods of entrepreneurship can be used pedagogical in a learning environment. The page will also support the user with examples of different teaching programs and other examples of best practice.

Pedagogical entrepreneurship is not about business and men in suits. It's a method for learning. The focus in the design should be on school, education and new ways of learning.

The final product should be motivating and engaging, but at the same time governmental and serious. We are not looking for something "flashy" and corporate-looking, but a moderate, task-focused and clean design that state quality.

We need designs for three pages:
1 - frontpage
2 - subpage ("Metoder og undervisningsopplegg")
3 - subpage ("Smått-VERK i Brekkelia")

The interaction design for these three pages will be uploaded as an attachment.

We would like you to find inspiration in the following websites:
- www.gryvekst.no
- www.lavrek.no
- www.tovandstudio.com
- www.kvp.no
(more will be added)

Please use the attached logo, and feel free to use this as an inspiration for the rest of the design.

Target Market(s)

Teachers

Industry/Entity Type

Education

Requirements
Must have
• * Header with: Logo. Main navigation. Utility navigation. Search box.
* Footer
Should not have
• Images of men in suits.
Very strong graphical elements that stands out too much (we want it clean).

```html
<!DOCTYPE html>
<html lang="en">
<head>
<meta charset="utf-8">
<title>Lorvika.no – Pedagogical entrepreneurship</title>
<link rel="stylesheet" href="https://fonts.googleapis.com/css2?family=Source+Sans+3:wght@400;600;700&display=swap">
<style>
:root{
  --page:#0c4a78;
  --header:#0a4470;
  --hero:#0d4e80;
  --panel:#2a6f9f;
  --panel-edge:#3d82b2;
  --line:#1d5d8c;
  --ink-light:#ffffff;
  --ink-soft:#cfe2f1;
  --ink-dark:#0f3554;
  --ink-muted:#2f5777;
  --accent:#2a8fd0;
  --logo:#4aa6e8;
  --search:#1f74b0;
}
*{box-sizing:border-box;margin:0;padding:0}
html,body{width:1200px;height:1200px;overflow:hidden}
body{background:var(--page);font-family:"Source Sans 3",sans-serif;color:var(--ink-light);position:relative}
.abs{position:absolute}
.site-header{left:0;top:0;width:1200px;height:111px;background:var(--header);box-shadow:0 6px 14px rgba(0,0,0,.35)}
.utility-nav{right:130px;top:8px;display:flex;font-size:14px;gap:0}
.utility-nav a{color:var(--ink-light);text-decoration:none;padding:0 14px;border-left:1px solid var(--ink-light);line-height:16px}
.utility-nav a:first-child{border-left:none;padding-bottom:4px;border-bottom:1px solid var(--accent)}
.utility-nav a:last-child{padding-right:0}
.brand{left:132px;top:26px;display:flex;align-items:center;gap:14px}
.brand-mark{width:52px;height:52px;border-radius:50%;background:var(--logo)}
.brand-name{font-size:50px;font-weight:700;color:var(--logo);line-height:1;letter-spacing:-1px}
.brand-tag{left:222px;top:77px;font-size:10.5px;color:var(--ink-light)}
.search{left:831px;top:59px;width:238px;height:28px;background:var(--search);border:1px solid #2e86c2;border-radius:3px;box-shadow:inset 0 1px 3px rgba(0,0,0,.4)}
.search svg{position:absolute;right:7px;top:5px}
.hero{left:0;top:111px;width:1200px;height:380px;background:var(--hero);box-shadow:0 10px 18px rgba(0,0,0,.3)}
.hero-text{left:139px;top:152px;width:460px;font-size:32px;line-height:45px;color:var(--ink-light)}
.hero-text strong{font-weight:700}
.btn-more{left:141px;top:373px;width:257px;height:40px;background:linear-gradient(#fff,#e3e9ee);border-radius:3px;color:var(--ink-dark);font-size:19px;display:flex;align-items:center;justify-content:center;gap:10px;box-shadow:0 2px 4px rgba(0,0,0,.35)}
.btn-reflect{left:141px;top:415px;width:257px;height:22px;background:linear-gradient(rgba(255,255,255,.12),rgba(255,255,255,0))}
.bubble{left:573px;top:141px;width:497px;height:297px}
.bubble-body{left:609px;top:141px;width:461px;height:297px;background:#fff;border-radius:3px}
.bubble-title{left:609px;top:164px;width:461px;text-align:center;font-size:28px;color:var(--ink-dark)}
.bubble-art{left:779px;top:217px;width:129px;height:129px;border-radius:50%;background:radial-gradient(circle at 40% 35%,#b8d6ee,#5b8fbf 70%,#3e6f9d)}
.bubble-caption{left:609px;top:359px;width:461px;text-align:center;font-size:22px;color:var(--ink-muted)}
.dot{top:415px;width:16px;height:16px;border-radius:50%}
.box{top:519px;height:202px;background:linear-gradient(var(--panel) 55%,rgba(42,111,159,0));border-top:1px solid var(--panel-edge);border-radius:3px 3px 0 0}
.gauge-box{left:131px;width:278px}
.gauge-q{left:131px;top:531px;width:278px;text-align:center;font-size:17px;line-height:24px;color:var(--ink-dark)}
.gauge-icon{left:140px;top:599px}
.gauge-cta{left:219px;top:596px;font-size:27px;line-height:35px}
.start-box{left:431px;width:638px}
.start-title{left:431px;top:597px;width:188px;text-align:center;font-size:23px}
.start-divider{left:620px;top:530px;width:1px;height:150px;background:#1f5a86}
.list-col{top:535px;font-size:13px;line-height:20px}
.list-col h3{font-weight:400;font-size:15px;color:var(--ink-dark);margin-bottom:8px}
.rule{left:0;top:736px;width:1200px;height:1px;background:var(--line)}
.inspiration{left:130px;top:754px;width:939px;height:184px;background:#0e4f80;border:1px solid var(--line);border-radius:3px;box-shadow:inset 0 0 18px rgba(0,0,0,.35)}
.inspiration-title{left:177px;top:766px;font-size:23px}
.card{top:807px;width:271px;height:105px;background:linear-gradient(#fff 60%,#dde4ea);border-radius:3px}
.card-photo{position:absolute;left:9px;top:9px;width:129px;height:88px;border:1px solid #8aa3b8;background:linear-gradient(#d6e0e8 0,#e8eef2 45%,#9a8b7a 70%,#f2f2f2 100%)}
.card-title{position:absolute;left:153px;top:8px;font-size:15.5px;line-height:24px;color:var(--ink-dark)}
.arrow{top:845px}
.footer-rule{left:0;top:958px;width:1200px;height:1px;background:var(--line)}
.footer-mark{left:132px;top:978px;width:56px;height:56px;border-radius:50%;background:#c4d6e4}
.fcol{top:966px;font-size:13px;line-height:24px}
.fcol h4{font-size:13.5px;font-weight:700;margin-bottom:7px}
.fdiv{top:968px;width:1px;height:142px;background:#0a3d64}
.more{top:1090px;font-size:13px}
</style>
</head>
<body>
<header class="site-header abs"></header>
<nav class="utility-nav abs">
  <a>Best Practice Schools</a><a>Lorvikameter</a><a>About lorvika. no</a>
</nav>
<div class="brand abs"><span class="brand-mark"></span><span class="brand-name">Lorvika</span></div>
<div class="brand-tag abs">Entreprenørielle metoder i undervisningen</div>
<div class="search abs">
  <svg width="18" height="18" viewBox="0 0 18 18"><circle cx="7.5" cy="7.5" r="5.5" fill="none" stroke="#0b3e66" stroke-width="2"/><line x1="11.5" y1="11.5" x2="16" y2="16" stroke="#0b3e66" stroke-width="2.2"/></svg>
</div>

<section class="hero abs"></section>
<p class="hero-text abs"><strong>Pedagogical entrepreneurship</strong> works. Lorem ipsum dolor sit amet, consectetuer adipiscing elit, sed diam nonummy nibh.</p>
<div class="btn-more abs">Learn more
  <svg width="18" height="16" viewBox="0 0 18 16"><rect width="18" height="16" rx="3" fill="#2a8fd0"/><path d="M4 8h7M8 4.5 11.5 8 8 11.5" stroke="#fff" stroke-width="2" fill="none"/></svg>
</div>
<div class="btn-reflect abs"></div>

<svg class="bubble abs" viewBox="0 0 497 297"><path d="M0 252 L40 222 L40 282 Z" fill="#fff"/></svg>
<div class="bubble-body abs"></div>
<div class="bubble-title abs">Learn about what, why and how!</div>
<div class="bubble-art abs" role="img" aria-label="Illustration of a puzzled round character with a question mark"></div>
<div class="bubble-caption abs">What is pedagocical entrepreneurship ?</div>
<span class="dot abs" style="left:986px;background:#0c3d63"></span>
<span class="dot abs" style="left:1012px;background:#9a9a9a"></span>

<div class="box gauge-box abs"></div>
<div class="gauge-q abs">Are you working<br>entrepreneurship - like ?</div>
<svg class="gauge-icon abs" width="70" height="70" viewBox="0 0 70 70">
  <circle cx="35" cy="35" r="33" fill="#8a9aa6"/><circle cx="35" cy="35" r="28" fill="#3a4650"/>
  <path d="M14 40a22 22 0 0 1 4-17" stroke="#3aa0e0" stroke-width="4" fill="none"/>
  <path d="M22 17a22 22 0 0 1 26 0" stroke="#8fd0f0" stroke-width="4" fill="none"/>
  <path d="M52 23a22 22 0 0 1 4 17" stroke="#e87a2a" stroke-width="4" fill="none"/>
  <line x1="35" y1="38" x2="35" y2="20" stroke="#dfe6ea" stroke-width="3"/><circle cx="35" cy="40" r="4" fill="#dfe6ea"/>
</svg>
<div class="gauge-cta abs">Try the<br>lorvikameter !</div>

<div class="box start-box abs"></div>
<div class="start-title abs">Get Started</div>
<div class="start-divider abs"></div>
<div class="list-col abs" style="left:657px">
  <h3>Methods</h3>
  Lorem ipsum dolor sit amet<br>Lorem ipsum dolor sit amet<br>Lorem ipsum dolor sit amet<br>Lorem ipsum dolor sit amet<br>Lorem ipsum dolor sit amet
</div>
<div class="list-col abs" style="left:869px">
  <h3>Teaching Plans</h3>
  Lorem ipsum dolor sit amet<br>Lorem ipsum dolor sit amet<br>Lorem ipsum dolor sit amet<br>Lorem ipsum dolor sit amet<br>Lorem ipsum dolor sit amet
</div>

<div class="rule abs"></div>
<section class="inspiration abs"></section>
<div class="inspiration-title abs">Inspiration</div>
<svg class="arrow abs" style="left:138px" width="28" height="30" viewBox="0 0 28 30"><path d="M28 0A15 15 0 0 0 28 30Z" fill="#1f6aa0"/><path d="M22 8 15 15 22 22" stroke="#fff" stroke-width="3" fill="none"/></svg>
<svg class="arrow abs" style="left:1030px" width="28" height="30" viewBox="0 0 28 30"><path d="M0 0A15 15 0 0 1 0 30Z" fill="#1f6aa0"/><path d="M6 8 13 15 6 22" stroke="#fff" stroke-width="3" fill="none"/></svg>
<div class="card abs" style="left:173px"><div class="card-photo" role="img" aria-label="Photo of a school building in winter with pupils outside"></div><div class="card-title">Smått-VERK at<br>Brekkelia school</div></div>
<div class="card abs" style="left:465px"><div class="card-photo" role="img" aria-label="Photo of a school building in winter with pupils outside"></div><div class="card-title">Smått-VERK at<br>Brekkelia school</div></div>
<div class="card abs" style="left:757px"><div class="card-photo" role="img" aria-label="Photo of a school building in winter with pupils outside"></div><div class="card-title">Smått-VERK at<br>Brekkelia school</div></div>

<div class="footer-rule abs"></div>
<div class="footer-mark abs"></div>
<div class="fcol abs" style="left:202px"><h4>Pedagogical entrepreneurship</h4>What is pedagogical entrepreneurship ?<br>Science<br>Best practice schools<br>Lorvikameteret<br>About lorvika.no</div>
<div class="fdiv abs" style="left:480px"></div>
<div class="fcol abs" style="left:539px"><h4>Methods</h4>Story Line<br>REAL<br>Cafe pedagogikk</div>
<div class="more abs" style="left:575px">See more...</div>
<div class="fdiv abs" style="left:681px"></div>
<div class="fcol abs" style="left:732px"><h4>Teaching Plans</h4>Title<br>Title<br>Title</div>
<div class="more abs" style="left:768px">See more...</div>
<div class="fdiv abs" style="left:873px"></div>
<div class="fcol abs" style="left:900px"><h4>Gode eksempler</h4>Smått-VERK at Brekkelia school<br>Smått-VERK at Brekkelia school<br>Smått-VERK at Brekkelia school</div>
<div class="more abs" style="left:936px">See more...</div>
</body>
</html>
```